Wooden Floor Website

I'd like a Modern and crisp site with emphasis on the site being easy to navigate through - services that we offer, gallery of previous work, history, who we are, contact, etc
https://tmqrvx8219067-my.dokshelfbox.net/:b:/g/personal/marcus_bellhaven_co_uk/QWT7K2_pmRsNaHXdovtYBeLWCKjuP9e3F6kRMZbqUwnPzs

Coding

Coded - Design and coding required

Number of Pages Required

5+ page

Requirements
Must have
• Word Press Site

```html
<!DOCTYPE html>
<html lang="en">
<head>
<meta charset="utf-8">
<title>Bellhaven Flooring — Exceptional Bespoke Floors</title>
<link href="https://fonts.googleapis.com/css2?family=IBM+Plex+Sans:ital,wght@0,400;0,500;0,600;0,700;1,500;1,600&family=Arimo:wght@400;700&display=swap" rel="stylesheet">
<style>
:root{
  --orange:#f18a1c;
  --brown-text:#8a5526;
  --ink:#222;
  --body:#444;
  --grey-bg:#f4f4f4;
  --white:#fff;
}
*{margin:0;padding:0;box-sizing:border-box}
html,body{width:1200px;height:3214px;overflow:hidden;background:var(--white)}
body{position:relative;font-family:"Arimo",Arial,sans-serif;color:var(--body)}
.abs{position:absolute}

/* header */
.site-header{left:0;top:0;width:1200px;height:120px;background:var(--white)}
.brand{left:111px;top:88px;display:flex;align-items:center;gap:8px}
.brand-square{width:12px;height:12px;background:var(--ink)}
.brand-name{font-family:"IBM Plex Sans",sans-serif;font-weight:700;font-size:16px;color:var(--ink);letter-spacing:.3px}
.main-nav{left:576px;top:52px;display:flex;font-family:"IBM Plex Sans",sans-serif;font-size:13.5px;font-weight:500;color:var(--ink)}
.main-nav span{display:inline-block}
.main-nav .n1{width:95px;color:var(--orange)}
.main-nav .n2{width:120px}
.main-nav .n3{width:120px}
.main-nav .n4{width:94px}

/* hero */
.hero{left:0;top:120px;width:1200px;height:615px;background:linear-gradient(180deg,#1f2d2c 0%,#2a3533 45%,#4a3c30 75%,#5c4a3a 100%)}
.hero-title{left:0;top:558px;width:1200px;text-align:center;font-family:"IBM Plex Sans",sans-serif;font-weight:700;font-size:51px;color:var(--orange);letter-spacing:1px}
.hero-sub{left:0;top:626px;width:1200px;text-align:center;font-family:"IBM Plex Sans",sans-serif;font-size:34px;color:var(--white);letter-spacing:.5px}
.hero-dots{left:575px;top:707px;display:flex;gap:7px}
.hero-dots i{display:block;width:11px;height:11px;border-radius:50%;background:var(--orange)}
.hero-dots i.on{background:var(--white)}

/* about */
.about-title{left:111px;top:851px;font-family:"IBM Plex Sans",sans-serif;font-weight:500;font-size:27px;color:var(--brown-text)}
.about-lead{left:111px;top:904px;width:420px;font-family:"IBM Plex Sans",sans-serif;font-style:italic;font-weight:600;font-size:14px;line-height:28px;color:var(--orange)}
.about-text{left:111px;top:1006px;width:400px;font-size:12px;line-height:27px;color:var(--body)}
.about-frame{left:578px;top:795px;width:490px;height:370px;background:#c07a2f;padding:14px}
.about-frame .inner{width:100%;height:100%;border:5px solid var(--orange);background:linear-gradient(160deg,#d6d8d2 0%,#9a958a 40%,#6e5b45 65%,#a8794a 100%)}

/* section titles */
.section-title{left:0;width:1200px;text-align:center;font-family:"IBM Plex Sans",sans-serif;font-weight:500;font-size:28px;color:var(--brown-text)}
.rule{left:560px;width:80px;height:2px;background:var(--orange)}

/* textures */
.textures{left:0;top:1228px;width:1200px;height:465px;background:var(--grey-bg)}
.swatch{top:1340px;width:238px;height:213px}
.sw-brushed{background:linear-gradient(90deg,#c99a5e,#dcb27a 40%,#c8955a 70%,#d9ad74)}
.sw-aged{background:linear-gradient(90deg,#b98a55,#c99a63 50%,#a97b48)}
.sw-band{background:linear-gradient(90deg,#c79c68,#d8b184 50%,#c49562)}
.sw-fumed{background:linear-gradient(90deg,#2a2522,#3a322c 50%,#24201d)}
.tex-name{top:1571px;font-family:"IBM Plex Sans",sans-serif;font-weight:500;font-size:17px;color:var(--brown-text)}
.tex-desc{top:1601px;width:225px;font-size:12px;line-height:24px;color:var(--body)}

/* process */
.process{left:0;top:1693px;width:1200px;height:419px;background:linear-gradient(90deg,#f18a1c 0%,#e98422 45%,#b8702e 75%,#8e5a2c 100%)}
.process-title{color:var(--white);top:1737px}
.process-line{left:237px;top:1891px;width:731px;height:3px;background:var(--white)}
.step-circle{top:1831px;width:120px;height:120px;border-radius:50%;background:var(--white);display:flex;align-items:center;justify-content:center}
.step-name{top:1966px;width:230px;text-align:center;font-family:"IBM Plex Sans",sans-serif;font-weight:700;font-size:15px;color:var(--white)}
.step-desc{top:1999px;width:230px;text-align:center;font-size:11.5px;line-height:23px;color:var(--white)}

/* gallery */
.gallery-title{top:2156px}
.photo{width:318px;height:268px}
.g1{background:linear-gradient(180deg,#dcdcd8 0%,#b9a58a 45%,#3a3431 75%,#2c2826 100%)}
.g2{background:linear-gradient(180deg,#d8d3cb 0%,#8e7a62 40%,#a7703c 70%,#8d5a2c 100%)}
.g3{background:linear-gradient(180deg,#f2f0ec 0%,#d8cbb8 40%,#c9ab85 100%)}
.g4{background:linear-gradient(160deg,#a06a38 0%,#b98148 50%,#8b5a2e 100%)}
.g5{background:linear-gradient(160deg,#6d4a2a 0%,#a8733e 50%,#5f3e22 100%)}
.g6{background:linear-gradient(160deg,#3b4b52 0%,#c79868 55%,#b2824f 100%)}

/* footer */
.site-footer{left:0;top:2850px;width:1200px;height:364px;background:linear-gradient(90deg,#7a4e22,#83552a 50%,#744a20)}
.foot-mark{left:586px;top:2928px;width:28px;height:28px;background:var(--white)}
.foot-name{left:0;top:2996px;width:1200px;text-align:center;font-family:"IBM Plex Sans",sans-serif;font-weight:500;font-size:23px;color:var(--white);letter-spacing:.5px}
.foot-nav{left:0;top:3055px;width:1200px;text-align:center;font-family:"IBM Plex Sans",sans-serif;font-weight:600;font-size:12.5px;color:var(--white);word-spacing:2px}
.foot-nav b{font-weight:400;margin:0 20px}
.foot-contact{left:0;top:3110px;width:1200px;display:flex;justify-content:center;align-items:center;font-size:12.5px;color:var(--white)}
.foot-contact span{display:flex;align-items:center;gap:8px}
.foot-contact .sep{margin:0 22px}
.copyright{left:0;top:3155px;width:1200px;text-align:center;font-size:12px;color:var(--white)}
</style>
</head>
<body>

<header class="abs site-header">
  <div class="abs brand"><span class="brand-square"></span><span class="brand-name">BELLHAVEN FLOORING</span></div>
  <nav class="abs main-nav">
    <span class="n1">HOME</span><span class="n2">ABOUT US</span><span class="n3">SERVICES</span><span class="n4">NEWS</span><span>CONTACT US</span>
  </nav>
</header>

<section class="abs hero" role="img" aria-label="Living room with dark green wall, velvet sofa, plants and wide-plank oak floor"></section>
<h1 class="abs hero-title">BELLHAVEN FLOORING</h1>
<p class="abs hero-sub">CREATING EXCEPTIONAL BESPOKE FLOORS</p>
<div class="abs hero-dots"><i></i><i class="on"></i><i></i></div>

<h2 class="abs about-title">ABOUT BELLHAVEN FLOORING</h2>
<p class="abs about-lead">BELLHAVEN FLOORING offer a range of fully bespoke finished wood flooring in planks, herringbone blocks and chevrons; styles to suit any interior design.</p>
<p class="abs about-text">With endless options available, you can choose the design, dimensions, grade, texture, colour and finish all produced to order in the UK. Combining the finest sustainable certified European Oak with the latest state of the art machinery, finishing products and highly skilled colour technicians, we will together create your bespoke wood floor.</p>
<div class="abs about-frame"><div class="inner" role="img" aria-label="Open-plan kitchen with timber island and herringbone oak floor"></div></div>

<section class="abs textures"></section>
<h2 class="abs section-title" style="top:1256px">TEXTURES &amp; TREATMENTS</h2>
<div class="abs rule" style="top:1304px"></div>

<div class="abs swatch sw-brushed" style="left:111px" role="img" aria-label="Brushed oak texture"></div>
<div class="abs swatch sw-aged" style="left:357px" role="img" aria-label="Aged oak texture"></div>
<div class="abs swatch sw-band" style="left:604px" role="img" aria-label="Bandsawn oak texture"></div>
<div class="abs swatch sw-fumed" style="left:850px" role="img" aria-label="Fumed dark oak texture"></div>

<h3 class="abs tex-name" style="left:111px">Brushed</h3>
<h3 class="abs tex-name" style="left:357px">Aged</h3>
<h3 class="abs tex-name" style="left:604px">Bandsawn</h3>
<h3 class="abs tex-name" style="left:850px">Fumed</h3>
<p class="abs tex-desc" style="left:111px">Removing the soft grain enhances the texture of the timber.</p>
<p class="abs tex-desc" style="left:357px">Each piece of flooring is tumbled to achieve an authentic</p>
<p class="abs tex-desc" style="left:604px">Our bandsawn texture particularly suits retail and commercial projects.</p>
<p class="abs tex-desc" style="left:850px">100% Fumed - tones of deep dark brown /black.</p>

<section class="abs process"></section>
<h2 class="abs section-title process-title">THE BELLHAVEN FLOORING PROCESS</h2>
<div class="abs rule" style="top:1784px;background:var(--white)"></div>
<div class="abs process-line"></div>

<div class="abs step-circle" style="left:177px">
  <svg width="64" height="64" viewBox="0 0 64 64" fill="none" stroke="#f18a1c" stroke-width="3" stroke-linejoin="round" stroke-linecap="round">
    <path d="M10 46 L44 12 L52 20 L18 54 L8 56 Z"/><path d="M40 16 L48 24"/>
    <path d="M14 10 L54 50 L48 56 L8 16 Z"/><path d="M20 22 L24 18 M28 30 L32 26 M36 38 L40 34"/>
  </svg>
</div>
<div class="abs step-circle" style="left:420px">
  <svg width="64" height="64" viewBox="0 0 64 64" fill="none" stroke="#f18a1c" stroke-width="3" stroke-linejoin="round" stroke-linecap="round">
    <path d="M32 12 L46 19 L46 35 L32 42 L18 35 L18 19 Z"/><path d="M18 19 L32 26 L46 19 M32 26 L32 42"/>
    <path d="M10 30 C4 40 14 50 32 50 C48 50 58 42 54 32"/><path d="M26 46 L32 50 L27 55"/>
  </svg>
</div>
<div class="abs step-circle" style="left:665px">
  <svg width="64" height="64" viewBox="0 0 64 64" fill="none" stroke="#f18a1c" stroke-width="3" stroke-linejoin="round">
    <path d="M16 8 H48 V46 L32 56 L16 46 Z"/><path d="M32 16 L35 23 L42 23 L36.5 27.5 L39 34 L32 30 L25 34 L27.5 27.5 L22 23 L29 23 Z"/>
    <path d="M22 40 L32 46 L42 40"/>
  </svg>
</div>
<div class="abs step-circle" style="left:908px">
  <svg width="64" height="64" viewBox="0 0 64 64" fill="none" stroke="#f18a1c" stroke-width="5" stroke-linecap="round" stroke-linejoin="round">
    <path d="M50 24 A22 22 0 1 1 40 12"/><path d="M20 30 L30 40 L54 14"/>
  </svg>
</div>

<h3 class="abs step-name" style="left:122px">DESIGN</h3>
<h3 class="abs step-name" style="left:365px">DIMENSIONS</h3>
<h3 class="abs step-name" style="left:610px">GRADE</h3>
<h3 class="abs step-name" style="left:853px">FINISHES</h3>
<p class="abs step-desc" style="left:122px">Start creating your bespoke floor by choosing your design</p>
<p class="abs step-desc" style="left:365px">Choose the dimensionsavailable in your design</p>
<p class="abs step-desc" style="left:610px">Our range of designs are available in Prime and Rustic grades</p>
<p class="abs step-desc" style="left:853px">To create your bespoke floor choose your texture and treatment</p>

<h2 class="abs section-title gallery-title">PHOTO GALLERY</h2>
<div class="abs rule" style="top:2204px"></div>
<div class="abs photo g1" style="left:111px;top:2232px" role="img" aria-label="Kitchen dining area with dark stained plank floor"></div>
<div class="abs photo g2" style="left:440px;top:2232px" role="img" aria-label="Bedroom with warm oak plank floor"></div>
<div class="abs photo g3" style="left:769px;top:2232px" role="img" aria-label="Pale limed oak floor with basket and throw"></div>
<div class="abs photo g4" style="left:111px;top:2511px" role="img" aria-label="Living room with honey oak plank floor and side table"></div>
<div class="abs photo g5" style="left:440px;top:2511px" role="img" aria-label="Rich brown oak floor with brass trolley"></div>
<div class="abs photo g6" style="left:769px;top:2511px" role="img" aria-label="Blue armchair on natural oak floor"></div>

<footer class="abs site-footer"></footer>
<div class="abs foot-mark"></div>
<div class="abs foot-name">BELLHAVEN FLOORING</div>
<nav class="abs foot-nav">HOME<b>|</b>ABOUT US<b>|</b>SERVICES<b>|</b>NEWS<b>|</b>CONTACT US</nav>
<div class="abs foot-contact">
  <span><svg width="12" height="12" viewBox="0 0 24 24" fill="#fff"><path d="M6.6 10.8a15 15 0 0 0 6.6 6.6l2.2-2.2c.3-.3.7-.4 1-.2 1.1.4 2.3.6 3.6.6.6 0 1 .4 1 1V20c0 .6-.4 1-1 1A17 17 0 0 1 3 4c0-.6.4-1 1-1h3.5c.6 0 1 .4 1 1 0 1.3.2 2.5.6 3.6.1.3 0 .7-.2 1z"/></svg>Phone: +44(0)7700 900 418</span>
  <span class="sep">|</span>
  <span><svg width="13" height="10" viewBox="0 0 26 20" fill="#fff"><path d="M0 0h26v20H0z"/><path d="M1 1l12 10L25 1" stroke="#7a4e22" stroke-width="2" fill="none"/></svg>Email: info@bellhavenfloors.co.uk</span>
  <span class="sep">|</span>
  <span><svg width="10" height="13" viewBox="0 0 20 26" fill="#fff"><path d="M10 0a9 9 0 0 0-9 9c0 7 9 17 9 17s9-10 9-17a9 9 0 0 0-9-9zm0 12a3 3 0 1 1 0-6 3 3 0 0 1 0 6z"/></svg>43718 Lorem Ipsum Dummy Text Lorem</span>
</div>
<p class="abs copyright">© Copyright -2019 Bellhaven Flooring. All rights reserved.</p>

</body>
</html>
```